Catalogue design for Aluminium Panel and spray painting manufacturer based in Huizhou, China.

Metrovex is a trading company that represent Dansheng metal spraying industry that manufactures aluminium panels and extrusions of all kinds and PVDF coating.

We are a manufacturer and producer of aluminium panels and PVDF painting based in Huizhou, China. We produce aluminium panels that are use widely in subways, shopping malls and construction works both for interior and exterior usage.

Dan Sheng mainly deal with contractors and project managers business within Mainland China and Hong Kong with a select few clientele in Australia and Philippines. We are now looking to expand the business and reach further international businesses.

We therefore need a new brochure to introduce the new trading name Metrovex to further the sales strategy into international borders. As manufacturers are heavily based on credentials and certifications these must be displayed accordingly to gain trust within the construction market.

The following content will be required

1. Who we are and what we do, manufacturer of aluminium panels and PVDF coating.
2. a)Guide to our manufacturing process, bending, cutting, welding of aluminum panels
b)Guide to choice of painting powder coating or PVDF coating. (PVDF being the main choice)
3. a)Some technical information about the core product of aluminium of aluminum panels such as size dimensions, width of panels and grade of aluminium.
b)Information on PVDF painting and a colour chart of either RAL or PANTONE.
4. Projects undertaken and some photos, preferably in a grid 2 column layout as exampled on attached photo.
5. Certifications of factory and office address and contact info.

We are looking for design that can showcase our manufacturing process in a catalogue displaying a consistent colour design theme throughout.

A simple guide of the manufacturing process and including some technical specification about the aluminium panels such as width and maximum dimenstions etc.

Target Market(s)

Asean and south east asia.

Industry/Entity Type

Manufacturer

Contact Information for Business Card

To be in colour theme with the catalogue design. Contain logo and to draw more focus more on the web url.

Colors
ec1f27

Requirements
Must have
• Must include a colour theme that is striking throughout the catalogue and easy to look at graphical layout. A graphical view without too much text aside from the technical specifications.
• Certifications of manufacturer. ISO, Verlo Danth etc( as displayed within company profile PDF)
Nice to have
• A consistent usage of photos without too obvious generic building photos.
• A well displayed layout for each page.
• Perhaps a three toned colour theme that works according with the logo. Perhaps some red throughout on a black main colour. Contrasting colours without an overwash of one colour.
Should not have
• Generic photos of office people or overly enthusiastic business people.
• With Exception of photos shots of the factory workers.

```html
<!DOCTYPE html>
<html lang="en">
<head>
<meta charset="utf-8">
<title>Metrovex Catalogue – Pages 5–6</title>
<link rel="stylesheet" href="https://fonts.googleapis.com/css2?family=Merriweather:wght@700;900&family=Open+Sans:wght@400;600;700&display=swap">
<style>
  :root {
    --red: #ec1f27;
    --maroon: #9c151c;
    --ink: #2a2a2d;
    --charcoal: #3b3b3f;
    --paper: #f4f4f4;
    --body: #5a5a5a;
    --stage: #a4a4a4;
  }
  * { box-sizing: border-box; margin: 0; padding: 0; }
  html, body { width: 1200px; height: 900px; overflow: hidden; }
  body {
    background: var(--stage);
    font-family: "Open Sans", Arial, sans-serif;
    position: relative;
  }
  .spread {
    position: absolute;
    left: 20px; top: 245px;
    width: 1160px; height: 410px;
    display: flex;
    box-shadow: 0 10px 30px rgba(0,0,0,.25);
  }
  .page {
    position: relative;
    width: 580px; height: 410px;
    background: var(--paper);
    overflow: hidden;
  }
  .page--left { background: linear-gradient(to right, var(--paper) 90%, #e2e2e2); }
  .page--right { background: linear-gradient(to right, #e2e2e2, var(--paper) 10%); }
  .page__art { position: absolute; inset: 0; width: 580px; height: 410px; }
  .section-head {
    position: absolute; left: 100px; top: 190px;
    display: flex; flex-direction: column; align-items: flex-end;
  }
  .section-title {
    font-family: "Merriweather", Georgia, serif;
    font-weight: 900; font-size: 15.5px; line-height: 20px;
    color: var(--ink); text-transform: uppercase; white-space: nowrap;
  }
  .section-sub {
    margin-top: 2px;
    font-family: "Merriweather", Georgia, serif;
    font-weight: 700; font-size: 9.5px; line-height: 13px;
    color: var(--ink); white-space: nowrap;
  }
  .section-note {
    margin-top: 1px;
    font-size: 7px; line-height: 10px; color: var(--body); white-space: nowrap;
  }
  .steps {
    position: absolute;
    display: grid; grid-template-columns: repeat(3, 1fr); column-gap: 22px;
    font-size: 7.5px; line-height: 1.45; color: var(--body);
  }
  .page--left .steps { left: 22px; top: 250px; width: 536px; }
  .page--right .steps { left: 28px; top: 232px; width: 530px; }
  .step { margin-bottom: 8px; }
  .step__title {
    display: block; font-weight: 700; font-size: 8px;
    color: var(--maroon); margin-bottom: 2px;
  }
  .brand {
    position: absolute; left: 18px; bottom: 16px;
    display: flex; align-items: center; gap: 5px;
  }
  .brand__mark { width: 12px; height: 12px; background: var(--red); }
  .brand__name { font-weight: 700; font-size: 11px; color: var(--red); }
  .rule {
    position: absolute; left: 100px; right: 50px; bottom: 21px;
    height: 3px;
    background: repeating-linear-gradient(to right, var(--ink) 0 26px, transparent 26px 32px);
  }
  .folio {
    position: absolute; right: 0; bottom: 0;
    width: 36px; height: 34px;
    background: var(--ink); border-left: 4px solid var(--red);
    color: #fff; font-weight: 700; font-size: 15px;
    display: flex; align-items: center; justify-content: center;
  }
</style>
</head>
<body>
<main class="spread">

  <section class="page page--left">
    <svg class="page__art" viewBox="0 0 580 410">
      <defs>
        <linearGradient id="photoHall" x1="0" y1="0" x2="1" y2="1">
          <stop offset="0" stop-color="#4a3a30"/>
          <stop offset=".55" stop-color="#b09078"/>
          <stop offset="1" stop-color="#e6dcd2"/>
        </linearGradient>
      </defs>
      <polygon points="0,0 580,0 580,188 0,160" fill="url(#photoHall)" role="img" aria-label="Photo of a large public hall with a curved aluminium panel ceiling"/>
      <polygon points="0,0 180,0 0,95" fill="var(--ink)"/>
      <polygon points="0,0 120,0 0,58" fill="var(--maroon)"/>
      <line x1="0" y1="104" x2="200" y2="0" stroke="#fff" stroke-width="3"/>
      <polygon points="0,160 580,188 580,198 0,172" fill="var(--paper)"/>
      <polygon points="0,160 145,167 140,180 0,174" fill="var(--maroon)"/>
      <polygon points="490,184 580,189 580,228" fill="var(--ink)"/>
    </svg>

    <header class="section-head">
      <h2 class="section-title">Additional Remarks of the Process</h2>
      <p class="section-sub">Aluminium Panel Preparation</p>
      <p class="section-note">Surface cleaning is the first and most important step in the painting work.</p>
    </header>

    <div class="steps">
      <div>
        <p class="step"><span class="step__title">1) Outline Degrease 1</span>Soak panels in a mild degreasing bath to lift oils and residue from the surface before treatment.</p>
        <p class="step"><span class="step__title">2) Water Cleaning 1</span>Rinse panels with clean running water to remove any degreaser left on the metal.</p>
      </div>
      <div>
        <p class="step"><span class="step__title">3) Alkaline Degrease 2</span>Apply a second alkaline bath so the aluminium surface is fully clean and evenly etched.</p>
        <p class="step"><span class="step__title">4) Water Cleaning 2</span>After the second bath, rinse again with water to neutralise the panel surface.</p>
      </div>
      <div>
        <p class="step"><span class="step__title">5) Acid Cleaning</span>Dip panels in a light acid solution to remove oxide film and prepare the metal for conversion coating.</p>
        <p class="step"><span class="step__title">6) Water Cleaning 3</span>Rinse the acid-treated panels with running water until the surface shows no trace of solution.</p>
      </div>
    </div>

    <div class="brand"><span class="brand__mark"></span><span class="brand__name">Metrovex</span></div>
    <div class="rule"></div>
    <div class="folio">5</div>
  </section>

  <section class="page page--right">
    <svg class="page__art" viewBox="0 0 580 410">
      <defs>
        <linearGradient id="photoStation" x1="0" y1="0" x2="1" y2="0">
          <stop offset="0" stop-color="#25243a"/>
          <stop offset=".45" stop-color="#8e8a86"/>
          <stop offset="1" stop-color="#cfc8bc"/>
        </linearGradient>
      </defs>
      <polygon points="110,0 580,0 580,170 0,200 0,130" fill="url(#photoStation)" role="img" aria-label="Photo of a subway station concourse clad in aluminium panels"/>
      <polygon points="0,0 140,0 0,85" fill="var(--maroon)"/>
      <polygon points="0,85 140,0 190,0 0,130" fill="var(--ink)"/>
      <line x1="0" y1="135" x2="200" y2="0" stroke="#fff" stroke-width="3"/>
      <polygon points="470,175 580,140 580,180" fill="var(--ink)"/>
      <polygon points="0,200 580,170 580,180 0,212" fill="var(--charcoal)"/>
      <polygon points="0,206 580,178 580,210 0,222" fill="var(--maroon)"/>
      <polygon points="0,222 580,210 580,214 0,226" fill="var(--paper)"/>
    </svg>

    <div class="steps">
      <div>
        <p class="step"><span class="step__title">7) Passivation</span>Form a thin chemical conversion layer on the panel surface to improve paint adhesion and resist corrosion over many years of use.</p>
      </div>
      <div>
        <p class="step"><span class="step__title">8) Water Cleaning 4</span>Rinse off the conversion chemicals with clean water to stop the reaction on the panel.</p>
        <p class="step"><span class="step__title">9) Water Cleaning 5</span>Rinse the panels once more so no loose salts remain before the final clean.</p>
      </div>
      <div>
        <p class="step"><span class="step__title">10) Deionised Water Cleaning</span>Use deionised water for a last rinse so the surface is free of minerals before drying.</p>
        <p class="step"><span class="step__title">11) Bake Cure</span>Dry and cure the treated panels at a controlled temperature so they are ready for coating.</p>
      </div>
    </div>

    <div class="brand"><span class="brand__mark"></span><span class="brand__name">Metrovex</span></div>
    <div class="rule"></div>
    <div class="folio">6</div>
  </section>

</main>
</body>
</html>
```